Blast Off -

I need to launch a new website that more accurately reflects what we do as a business. We are an IT Reseller that specialises in delivering innovative solutions covering supply, implementation and support. My current website is www.tervanbnr.com and was something I designed myself on the Web Wren website. This was fine for the first 2 years but now I need something more professional and detailed. A couple of websites for companies similar to Tervan BNR are www.dranvolt.co.uk and www.mirendaway.co.uk. By looking at these it will hopefully give you an idea as to what I am trying to achieve.

Target Market(s)

UK based companies with between 30-250 employees, no fixed vertical

Coding

Coded - Design and coding required

Number of Pages Required

4 page

Font styles to use
Sans Serif

Colors
33a6d7
0592cd
85cae6

Requirements
Must have
• Contact details page to include a "Get in touch with us " section, About Us page, IT Support page to include the headings 1/ Proactive Monitoring 2/ 24 x 7 Support 3/ Security and Data Back-up 4/ Built-in Compliance (GDPR) 5/ Responsive IT Support. I am happy to provide the wording for these headings.
Clean crisp home screen with a Menu offering the requested drop down options.
Nice to have
• Easy to navigate site with a good flow. I have updated a page regarding cloud services, this would be great to have as a separate drop down menu option. I would like to have different Cloud logo's in ideally the Tervan Blue colour. Can you please add the photograph of Penhorrow Hall which is my office in the contact us page.
Should not have
• I definitely DO NOT want a photo/view of London on the home page!!

```html
<!DOCTYPE html>
<html lang="en">
<head>
<meta charset="utf-8">
<title>Tervan BNR – IT Consulting</title>
<link href="https://fonts.googleapis.com/css2?family=Montserrat:ital,wght@0,400;0,500;0,600;0,700;1,400&display=swap" rel="stylesheet">
<style>
:root{
  --blue:#0592cd;
  --blue-mid:#33a6d7;
  --blue-light:#85cae6;
  --ink:#222b33;
  --muted:#8a9097;
  --grey-band:#f3f3f3;
  --page:#fafcfd;
  --white:#ffffff;
  --line:#e3e6e9;
}
*{box-sizing:border-box;margin:0;padding:0}
html,body{width:1200px;height:3876px;overflow:hidden}
body{position:relative;background:var(--page);font-family:'Montserrat',sans-serif;color:var(--ink)}
.abs{position:absolute}
.center{text-align:center}

.brand-top{left:38px;top:40px;display:flex;align-items:center;gap:16px}
.brand-top .dot{width:74px;height:74px;border-radius:50%;background:var(--blue)}
.brand-top span{font-size:28px;font-weight:600;letter-spacing:1px;color:var(--ink)}

.site{left:91px;top:175px;width:1014px;height:3615px;background:var(--white);box-shadow:0 0 30px rgba(5,146,205,.08);overflow:hidden}

.nav{left:0;top:0;width:1014px;height:51px;background:var(--white)}
.nav .logo{left:148px;top:13px;display:flex;align-items:center;gap:8px;font-size:12px;font-weight:600}
.nav .logo i{width:26px;height:26px;border-radius:50%;background:var(--blue);display:block}
.nav ul{position:absolute;left:455px;top:19px;display:flex;gap:30px;list-style:none;font-size:10px}
.nav li.active{color:var(--blue);font-weight:600}

.hero{left:0;top:51px;width:1014px;height:519px;background:linear-gradient(180deg,#5b93b5 0%,#4f86a8 60%,#3f7193 100%)}
.hero h1{left:0;top:120px;width:1014px;font-size:33px;font-weight:600;color:var(--white)}
.hero p{left:0;top:172px;width:1014px;font-size:9px;line-height:15px;color:var(--white)}
.btn{display:block;background:var(--blue);color:var(--white);font-size:10px;font-weight:600;text-align:center;line-height:33px;height:33px;border-radius:2px}
.hero .btn{left:461px;top:214px;width:93px}

.features{left:84px;top:488px;width:846px;height:165px;background:var(--white);box-shadow:0 6px 24px rgba(0,0,0,.08);display:flex;padding:40px 0 0}
.feature{flex:1;text-align:center;border-right:1px solid var(--line);height:75px}
.feature:last-child{border:none}
.feature svg{display:block;margin:-12px auto 8px}
.feature h4{font-size:10px;font-weight:500;margin-bottom:14px}
.feature p{font-size:8px;line-height:12px;color:var(--muted)}

.section-title{font-size:29px;font-weight:600;color:var(--ink)}
.section-sub{font-size:9px;line-height:15px;color:var(--muted)}

.approach h3{font-size:19px;font-weight:500}
.approach p{font-size:9px;line-height:15px;color:var(--muted);width:250px;margin-top:18px}
.arrows{display:flex;gap:18px}

.photo{background:linear-gradient(135deg,#c9ccc8,#8d8f8a)}

.grey-band{left:0;top:1157px;width:1014px;height:568px;background:var(--grey-band)}
.services{left:48px;top:1361px;width:920px;display:flex}
.service{flex:1;text-align:center}
.service .ring{width:66px;height:66px;border-radius:50%;background:var(--white);margin:0 auto 20px;display:flex;align-items:center;justify-content:center;box-shadow:0 3px 12px rgba(0,0,0,.06)}
.service h4{font-size:10px;font-weight:500;margin-bottom:10px}
.service p{font-size:8px;line-height:13px;color:var(--muted);width:150px;margin:0 auto}

.connect{left:191px;top:1599px;width:633px;height:251px;background:var(--white);box-shadow:0 4px 20px rgba(0,0,0,.08)}
.connect h2{margin-top:46px}
.connect p{font-size:9px;line-height:15px;color:var(--muted);margin:16px auto 0;width:540px}
.connect .btn{position:absolute;left:270px;top:173px;width:93px}

.card{width:210px;height:161px;background:#f7f8f9;padding:18px 12px}
.card .num{position:absolute;right:14px;top:12px;font-size:50px;font-weight:600;color:var(--blue-light);opacity:.6}
.card .ico{width:44px;height:44px;border-radius:50%;background:var(--white);display:flex;align-items:center;justify-content:center}
.card h4{font-size:12px;font-weight:600;margin-top:12px}
.card p{font-size:8px;line-height:13px;color:var(--muted);margin-top:10px}
.card.active{background:var(--blue)}
.card.active h4,.card.active p{color:var(--white)}
.card.active .num{color:var(--white);opacity:.2}

.testimonials{left:0;top:2508px;width:1014px;height:1107px;background:var(--blue)}
.testimonials h2{color:var(--white);font-size:30px;font-weight:600}
.testimonials blockquote{font-size:20px;line-height:29px;font-style:italic;color:var(--white)}
.testimonials .who{color:var(--white);font-size:12px;font-weight:600}
.testimonials .who small{font-size:9px;font-weight:400}

.contact{left:147px;top:537px;width:720px;height:355px;display:flex}
.contact .hall{width:348px;height:355px;background:linear-gradient(180deg,#6f8a9a 0%,#7a5e4a 55%,#4b4a3a 100%);position:relative}
.contact .map{width:372px;height:355px;background:linear-gradient(135deg,#e8efe6,#d6e4d3)}
.hall h3{position:absolute;left:36px;top:74px;color:var(--white);font-size:16px;font-weight:500;line-height:20px}
.field{position:absolute;left:36px;width:236px;background:var(--white);font-size:7px;color:var(--muted);padding:8px 14px}
.hall .btn{position:absolute;left:36px;top:261px;width:77px;height:30px;line-height:30px;font-size:8px}

.footer .logo{display:flex;align-items:center;gap:8px;color:var(--white);font-size:13px;font-weight:600}
.footer .logo i{width:26px;height:26px;border-radius:50%;background:var(--white);display:block;opacity:.85}
.footer .info{color:var(--white);font-size:7px;line-height:10px;display:flex;gap:10px;align-items:flex-start}
.footer ul{list-style:none;color:var(--white);font-size:9px;line-height:19px}
.footer h5{color:var(--white);font-size:10px;font-weight:600}
.footer .input{background:var(--white);font-size:8px;color:var(--muted);width:144px;height:34px;line-height:34px;padding-left:18px}
.footer .subscribe{background:#0a6f9d;color:var(--white);font-size:10px;width:96px;height:34px;line-height:34px;text-align:center}
.footer .legal{color:var(--white);font-size:6px;word-spacing:2px}
.footer .rule{height:1px;background:rgba(255,255,255,.35)}
</style>
</head>
<body>

<div class="abs brand-top"><div class="dot"></div><span>Tervan BNR</span></div>

<main class="abs site">

  <header class="abs nav">
    <div class="abs logo"><i></i>Tervan BNR</div>
    <ul>
      <li class="active">Home</li>
      <li>About Us</li>
      <li>IT Support ⌄</li>
      <li>Cloud Adoption ⌄</li>
      <li>Contact Us</li>
    </ul>
  </header>

  <section class="abs hero" role="img" aria-label="Team of colleagues stacking hands together over a meeting table">
    <h1 class="abs center">Experienced, Personalised IT Consulting</h1>
    <p class="abs center">We understand that no two businesses are the same so why should the service delivered be any different.<br>We aim to understand all your business drivers so advise you every step of the way.</p>
    <span class="abs btn">Get Started</span>
  </section>

  <div class="abs features">
    <div class="feature">
      <svg width="20" height="20" viewBox="0 0 20 20" fill="none" stroke="#0592cd" stroke-width="1.2"><circle cx="10" cy="10" r="8"/><path d="M10 5v10M12.5 7.5c0-1-1-1.6-2.5-1.6s-2.5.7-2.5 1.8 1 1.5 2.5 1.8 2.5.8 2.5 1.9-1 1.8-2.5 1.8-2.5-.7-2.5-1.7"/></svg>
      <h4>Save Time</h4><p>We can allow you to<br>focus solely on growing</p>
    </div>
    <div class="feature">
      <svg width="24" height="20" viewBox="0 0 24 20" fill="none" stroke="#0592cd" stroke-width="1.2"><circle cx="9" cy="9" r="7"/><path d="M9 5v4l3 2M17 14l5 5"/></svg>
      <h4>24/7 Support</h4><p>Allow us to deliver the<br>support and expertise.</p>
    </div>
    <div class="feature">
      <svg width="20" height="20" viewBox="0 0 20 20" fill="none" stroke="#0592cd" stroke-width="1.2"><path d="M2 18h16M4 14l4-4 3 3 6-7M13 6h4v4"/></svg>
      <h4>Budgeting</h4><p>Take out the support<br>contract that best suits</p>
    </div>
    <div class="feature">
      <svg width="20" height="20" viewBox="0 0 20 20" fill="none" stroke="#0592cd" stroke-width="1.2"><circle cx="10" cy="4" r="2.5"/><circle cx="4" cy="15" r="2.5"/><circle cx="16" cy="15" r="2.5"/><circle cx="10" cy="15" r="2.5"/><path d="M10 7v5M4 12V10h12v2"/></svg>
      <h4>Risk Management</h4><p>Leave us to protect your<br>business, if there is an</p>
    </div>
  </div>

  <h2 class="abs section-title center" style="left:0;top:732px;width:1014px">About Us</h2>
  <p class="abs section-sub center" style="left:0;top:779px;width:1014px">We understand that no two businesses are the same so why should the service delivered be any different.<br>We aim to understand all your business drivers so advise you every step of the way.</p>

  <div class="abs approach" style="left:147px;top:860px">
    <h3>Our Approach</h3>
    <p>We understand that no two businesses are the same so why should the service delivered be any different. We aim to understand all your business drivers so we can not only add a world class services but be there to advise you every step of the way.</p>
    <div class="arrows" style="margin-top:40px">
      <svg width="18" height="18" viewBox="0 0 18 18" fill="none" stroke="#85cae6" stroke-width="1.3"><circle cx="9" cy="9" r="8"/><path d="M10.5 5.5 7 9l3.5 3.5"/></svg>
      <svg width="18" height="18" viewBox="0 0 18 18" fill="none" stroke="#0592cd" stroke-width="1.3"><circle cx="9" cy="9" r="8"/><path d="M7.5 5.5 11 9l-3.5 3.5"/></svg>
    </div>
  </div>

  <div class="abs photo" style="left:512px;top:860px;width:225px;height:162px" role="img" aria-label="Colleagues in a bright meeting room around a conference table"></div>
  <div class="abs photo" style="left:759px;top:929px;width:108px;height:78px" role="img" aria-label="Business team in a boardroom discussion"></div>
  <div class="abs photo" style="left:678px;top:1010px;width:144px;height:67px" role="img" aria-label="Team meeting in an office"></div>

  <div class="abs grey-band"></div>
  <h2 class="abs section-title center" style="left:0;top:1234px;width:1014px">IT Support - Infrastructure Support</h2>
  <p class="abs section-sub center" style="left:0;top:1283px;width:1014px">Using A Pro Fessional And Friendly IT Support Company To Look After Your IT Infrastructure Is A Cost Effective Way To Have All The Skills<br>Available When Needed, But Without Having The Overheads Associated With Full Time Staff.</p>

  <div class="abs services">
    <div class="service">
      <div class="ring"><svg width="40" height="26" viewBox="0 0 40 26" fill="none" stroke="#0592cd" stroke-width="1.4"><path d="M2 13C8 4 32 4 38 13 32 22 8 22 2 13Z"/><circle cx="20" cy="13" r="6"/><circle cx="20" cy="13" r="2.5"/></svg></div>
      <h4>Proactive Monitoring</h4><p>We can allow you to focus solely on growing and developing your business.</p>
    </div>
    <div class="service">
      <div class="ring"><svg width="26" height="30" viewBox="0 0 26 30" fill="none" stroke="#0592cd" stroke-width="1.4"><path d="M13 2 23 6v9c0 6-5 11-10 13C8 26 3 21 3 15V6Z"/><rect x="9" y="13" width="8" height="7"/><path d="M10.5 13v-2a2.5 2.5 0 0 1 5 0v2"/></svg></div>
      <h4>Security and Data Back-up</h4><p>We can allow you to focus solely on growing and developing your business.</p>
    </div>
    <div class="service">
      <div class="ring"><svg width="30" height="30" viewBox="0 0 30 30" fill="none" stroke="#0592cd" stroke-width="1.4"><circle cx="15" cy="11" r="7"/><path d="M12 11l2 2 4-4M9 18l-3 8 5-2 2 4 2-7M21 18l3 8-5-2-2 4"/></svg></div>
      <h4>Built-in Compliance (GDPR)</h4><p>We can allow you to focus solely on growing and developing your business.</p>
    </div>
    <div class="service">
      <div class="ring"><svg width="30" height="30" viewBox="0 0 30 30" fill="none" stroke="#0592cd" stroke-width="1.4"><circle cx="15" cy="15" r="12"/><circle cx="15" cy="15" r="7"/><path d="M15 3v5M15 22v5M3 15h5M22 15h5"/></svg></div>
      <h4>Responsive IT Support</h4><p>We can allow you to focus solely on growing and developing your business.</p>
    </div>
  </div>

  <div class="abs connect center">
    <h2 class="section-title">Let's Get Connected</h2>
    <p>"To Keep Your Costs Down Tervan BNR Provides Flexible Options That Fit Your Requirements And Budgets, From Pre-Paid To Fully Managed Support. We Deliver Cost Effective IT Support For Companies Whether You Are Setup For Remote Working Or Are Office Based.We Can Also Tailor A Support Package Specifically For Your Business. So Please Call Us For A Chat Without Any Obligation On 01632 960104"</p>
    <span class="btn">Call Now</span>
  </div>

  <h2 class="abs section-title center" style="left:0;top:1934px;width:1014px">Cloud Adoption</h2>
  <p class="abs section-sub center" style="left:0;top:1981px;width:1014px">We understand that no two businesses are the same so why should the service delivered be any different.<br>We aim to understand all your business drivers so advise you every step of the way.</p>

  <div class="abs card active" style="left:147px;top:2061px">
    <span class="num">1</span>
    <div class="ico"><svg width="24" height="24" viewBox="0 0 24 24" fill="none" stroke="#0592cd" stroke-width="1.3"><circle cx="9" cy="8" r="3.5"/><path d="M3 19c0-3.5 2.7-6 6-6"/><circle cx="17" cy="16" r="3"/><path d="M17 11v2M17 19v2M12 16h2M20 16h2"/></svg></div>
    <h4>Services. Perfectly Managed</h4>
    <p>We employ Managed Services to significantly streamline your business, tailoring your solutions to meet digital market demands.</p>
  </div>
  <div class="abs card" style="left:402px;top:2061px">
    <span class="num">2</span>
    <div class="ico"><svg width="24" height="24" viewBox="0 0 24 24" fill="none" stroke="#0592cd" stroke-width="1.3"><path d="M4 12a8 8 0 0 1 14-5M20 12a8 8 0 0 1-14 5M18 3v4h-4M6 21v-4h4"/><circle cx="12" cy="12" r="2.5"/></svg></div>
    <h4>Fail Fast with the Cloud</h4>
    <p>Prototype your new business features within less than a week &amp; without having to invest a single penny.</p>
  </div>
  <div class="abs card" style="left:657px;top:2061px">
    <span class="num">3</span>
    <div class="ico"><svg width="26" height="24" viewBox="0 0 26 24" fill="none" stroke="#0592cd" stroke-width="1.3"><path d="M7 18H6a4.5 4.5 0 0 1-.5-9A6.5 6.5 0 0 1 18 7.5 5 5 0 0 1 20 18h-1"/><path d="M10 20v-4M13 20v-7M16 20v-5"/></svg></div>
    <h4>Improve your ROI</h4>
    <p>Using the Cloud, we launch your product to market quickly and cost-effectively – making sure it's future-proof, scalable, reliable, and</p>
  </div>
  <div class="abs card" style="left:275px;top:2268px">
    <span class="num">4</span>
    <div class="ico"><svg width="26" height="24" viewBox="0 0 26 24" fill="none" stroke="#0592cd" stroke-width="1.3"><path d="M7 18H6a4.5 4.5 0 0 1-.5-9A6.5 6.5 0 0 1 18 7.5 5 5 0 0 1 20 18H7Z"/><path d="M10 15v-3h2l2-3v6Z"/></svg></div>
    <h4>The Cloud Dream Team</h4>
    <p>They'll have thorough understanding of the project's scope. They'll see the bigger picture and understand the business value you want</p>
  </div>
  <div class="abs card" style="left:530px;top:2268px">
    <span class="num">5</span>
    <div class="ico"><svg width="24" height="24" viewBox="0 0 24 24" fill="none" stroke="#0592cd" stroke-width="1.3"><path d="M4 20V12h4v8M10 20V8h4v12M16 20V4h4v16M2 20h20"/></svg></div>
    <h4>The Business Benefits</h4>
    <p>Make informed decisions about the product's development pipeline. Save costs as you'll spend less time on redefining requirements.</p>
  </div>

  <section class="abs testimonials">
    <h2 class="abs center" style="left:0;top:80px;width:1014px">Testimonials</h2>
    <p class="abs center" style="left:0;top:126px;width:1014px;color:var(--white);font-size:9px">What our clint say about us</p>
    <svg class="abs" style="left:484px;top:205px" width="46" height="40" viewBox="0 0 46 40" fill="none" stroke="#ffffff" stroke-width="1.6"><path d="M20 38C10 30 4 22 4 14a8 8 0 0 1 16 0c0 5-4 8-8 8M42 38C32 30 26 22 26 14a8 8 0 0 1 16 0c0 5-4 8-8 8"/></svg>
    <blockquote class="abs center" style="left:100px;top:261px;width:814px">Our extensive equipment fleet, along with our modern maintenance and fabrication facility allow us the ability to support our diverse workforce and our capable partners whenever necessary.</blockquote>
    <svg class="abs" style="left:147px;top:369px" width="18" height="18" viewBox="0 0 18 18" fill="none" stroke="#fff" stroke-width="1.3"><circle cx="9" cy="9" r="8"/><path d="M10.5 5.5 7 9l3.5 3.5"/></svg>
    <p class="abs center who" style="left:0;top:370px;width:1014px">Owen Hartley <small>- Merrow Client</small></p>
    <svg class="abs" style="left:850px;top:369px" width="18" height="18" viewBox="0 0 18 18" fill="none" stroke="#fff" stroke-width="1.3"><circle cx="9" cy="9" r="8"/><path d="M7.5 5.5 11 9l-3.5 3.5"/></svg>

    <div class="abs contact">
      <div class="hall" role="img" aria-label="Photograph of Penhorrow Hall, the Tervan BNR office">
        <h3>Get in touch<br>with us</h3>
        <div class="field" style="top:124px;height:29px">Your Name</div>
        <div class="field" style="top:159px;height:28px">Phone Number</div>
        <div class="field" style="top:193px;height:52px;padding-top:20px">Write Message</div>
        <span class="btn">Get Started</span>
      </div>
      <div class="map" role="img" aria-label="Street map showing the office location"></div>
    </div>

    <div class="abs footer" style="left:147px;top:944px;width:720px;height:130px">
      <div class="abs logo" style="left:0;top:0">
        <i></i>Tervan BNR
      </div>
      <div class="abs info" style="left:0;top:42px">
        <svg width="10" height="10" viewBox="0 0 10 10" fill="#fff"><path d="M2 1 4 3 3 4.5C3.6 5.8 4.2 6.4 5.5 7L7 6l2 2-1 1.5C4.5 9.5.5 5.5.5 2Z"/></svg>
        <span>01632 960104</span>
      </div>
      <div class="abs info" style="left:0;top:62px">
        <svg width="10" height="12" viewBox="0 0 10 12" fill="#fff"><path d="M5 0a4 4 0 0 1 4 4c0 3-4 8-4 8S1 7 1 4a4 4 0 0 1 4-4Zm0 2.5a1.5 1.5 0 1 0 0 3 1.5 1.5 0 0 0 0-3Z"/></svg>
        <span>Penhorrow Hall, Ashmere Lane,<br>Fenbridge, Hertfordshire, FB2 4QX</span>
      </div>
      <ul class="abs" style="left:281px;top:-6px">
        <li>Home</li><li>About Us</li><li>IT Support</li><li>Cloud Adoption</li><li>Contact Us</li>
      </ul>
      <h5 class="abs" style="left:480px;top:-2px">Get the freshest news from us</h5>
      <div class="abs input" style="left:480px;top:17px">Your email address...</div>
      <div class="abs subscribe" style="left:624px;top:17px">Subscribe</div>
      <div class="abs rule" style="left:0;top:105px;width:720px"></div>
      <p class="abs legal" style="left:0;top:113px">Terms &amp; Conditions &nbsp;| &nbsp;Privacy Policy &nbsp;| &nbsp;Accessibility &nbsp;| &nbsp;Legal</p>
      <p class="abs legal" style="right:0;top:113px">Tervan BNR 2020. All right reserved</p>
    </div>
  </section>

</main>
</body>
</html>
```